Clean Modern Skin Product branding/ label.

I need a label for a skincare line. The company is Velunda but product names will vary. A couple products to list are:
Sensitive Cleanser, Clarel, Tovane, Olva up, Halden, Halden Plus, Halden Intense, Tamby, Morwen and Quillet.

I would like the color scheme to be muted greens, grays, tourquise. The bottles are white, boston shaped with pumps, and ounces are 2, 4, 8, 16 ounces. When I choose the design, I can give you exact label sizes. Along with the ingredience already on the product label.

The look I desire is clean, minimal. A modern, organic look. Ideas that come to mind are a Voravel,https://www.voravel-example.com/product/2841/66302/4-step/step-3-polish/glowing-tonic-2 and the simplicity of Osta Vi.

Both styles high light the name, in this case Velunda, and then the specific product.

My product is clean utilizing pure ingredients rather that a bunch fillers and binders. When I work with my clients I normally will say we need to "restore the balance" from over use of harsh products. That is why this lines works. It restores the skin to it's natural state. The process is simple, so I would like the label to reflect that simplicity.

Target Market(s)

Anyone with sensitive skin. So gender neutral

Industry/Entity Type

Skin Care Product

Font styles to use
Serif
Sans Serif
Decorative

Colors
acd037
33b8a4
fcfefd
85cae6
d3d3d3

Requirements
Must have
• Logo, name of product and color identity for cleanser, Active products, moisturizers
• I am thinking we could have one color for a cleanser and a space where I can put a sticker on which cleanser it is. Acne Cleasner, Sensitive Cleanser, and Cleanser.
Nice to have
• Not sure....suprise me. I would like the font to stay the same on the VELUNDA, but you can change color, or color of leaf.
Should not have
• Too busy, too crowded or look like every other skincare line

```html
<!DOCTYPE html>
<html lang="en">
<head>
<meta charset="utf-8">
<title>Velunda Sensitive Cleanser Label</title>
<link rel="stylesheet" href="https://fonts.googleapis.com/css2?family=Lato:wght@400;700;900&display=swap">
<style>
  :root {
    --label-top: #e4f3f3;
    --label-mid: #bfe3e3;
    --label-low: #8fd0ca;
    --label-base: #33b8a4;
    --ink-dark: #1c1c1c;
    --ink-soft: #2b2b2b;
    --rule: #f4fbfa;
  }
  * { margin: 0; padding: 0; box-sizing: border-box; }
  html, body {
    width: 1200px;
    height: 3468px;
    overflow: hidden;
  }
  body {
    font-family: "Lato", sans-serif;
    background: linear-gradient(180deg,
      var(--label-top) 0%,
      var(--label-mid) 40%,
      var(--label-low) 72%,
      var(--label-base) 100%);
    position: relative;
    color: var(--ink-dark);
  }
  .brand-name {
    position: absolute;
    top: 600px;
    left: 0;
    width: 1200px;
    text-align: center;
    font-family: "Lato", sans-serif;
    font-weight: 900;
    font-size: 168px;
    letter-spacing: -4px;
    line-height: 1;
    text-transform: lowercase;
    color: var(--ink-dark);
  }
  .product-name {
    position: absolute;
    top: 2740px;
    left: 0;
    width: 1200px;
    text-align: center;
    font-family: "Lato", sans-serif;
    font-weight: 400;
    font-size: 128px;
    line-height: 1.06;
    color: var(--ink-soft);
  }
  .divider {
    position: absolute;
    top: 3100px;
    left: 360px;
    width: 700px;
    height: 5px;
    background: var(--rule);
    opacity: 0.85;
  }
  .product-descriptor {
    position: absolute;
    top: 3150px;
    left: 0;
    width: 1200px;
    text-align: center;
    font-family: "Lato", sans-serif;
    font-weight: 400;
    font-size: 38px;
    line-height: 1.2;
    color: var(--ink-soft);
  }
</style>
</head>
<body>
  <main class="label">
    <h1 class="brand-name">velunda</h1>
    <h2 class="product-name">Sensitive<br>Cleanser</h2>
    <div class="divider"></div>
    <p class="product-descriptor">liquid facial soap<br>extra-mild</p>
  </main>
</body>
</html>
```